Meridel Advisory & Coaching Collective Web Site Design

Help!

We have started designing and building a Web site to promote and sell training services to HR managers. But we are not very good designers. In fact, we stink.

We have a logo.

We have most of the content (more or less) and the site architecture. But we have put together a pretty lousy look and feel.

Take a look: http://brightlowpath.example/vortalindex.html

What we'd like is a Web 3.0 type design - clean, simple, modern looking. Some sites we admire:

pinvale.example
trelosk.example
skivorn.example
quibbledot.example
morpa.example

We have access to stock photography, some of which we've used on the site we've built so far. You can use those and others. But keep it simple.

Target Market(s)

Professional HR managers in larger companies

Requirements
Must have
• Use our logo and a color scheme based off of it. Logo file uploaded.

Need to see home page and examples of secondary pages, based on site currently online.

```html
<!DOCTYPE html>
<html lang="en">
<head>
<meta charset="utf-8">
<title>BrightlowPath for Pellora – Home</title>
<link href="https://fonts.googleapis.com/css2?family=Yanone+Kaffeesatz:wght@300;400;500&display=swap" rel="stylesheet">
<style>
  :root{
    --nav-top:#2f5fbf;
    --nav-bottom:#1b3f95;
    --nav-pill:#0d2358;
    --brand-navy:#1c3f8f;
    --brand-ink:#222;
    --link-blue:#1a8fc8;
    --tab-blue:#3f6fd1;
    --heading-blue:#4a86e8;
    --hero-light:#a9bf50;
    --hero-dark:#6a8a12;
    --footer-bg:#efefef;
    --footer-text:#666;
    --rule:#d4d4d4;
    --chat-red:#c0322a;
  }
  *{box-sizing:border-box;margin:0;padding:0}
  html,body{width:1092px;height:1200px;overflow:hidden;background:#fff}
  body{font-family:'Yanone Kaffeesatz',sans-serif;color:var(--brand-ink);position:relative}

  .main-nav{position:absolute;left:0;top:0;width:1092px;height:58px;
    background:linear-gradient(var(--nav-top),var(--nav-bottom));
    box-shadow:0 2px 3px rgba(0,0,0,.25)}
  .main-nav ul{list-style:none;display:flex;align-items:center;justify-content:space-between;height:58px;padding:0 36px 0 33px}
  .main-nav li{color:#fff;font-size:24px;font-weight:400;letter-spacing:.3px;white-space:nowrap}
  .main-nav li.current{background:var(--nav-pill);border-radius:7px;padding:2px 12px}

  .brand{position:absolute;left:42px;top:100px;display:flex;align-items:center}
  .brand-dot{width:38px;height:38px;border-radius:50%;background:var(--heading-blue);margin-right:10px}
  .brand-name{font-size:54px;font-weight:400;color:var(--brand-navy);line-height:1}
  .brand-for{font-size:30px;color:var(--brand-ink);margin:12px 8px 0 10px}
  .partner-badge{width:104px;height:42px;background:#5a7fbf}

  .contact{position:absolute;left:835px;top:88px}
  .contact-row{display:flex;align-items:center;height:34px}
  .contact-row svg{margin-right:12px}
  .contact-phone{font-size:26px;color:var(--link-blue)}
  .contact-email{font-size:19px;color:var(--link-blue);text-decoration:underline}

  .hero{position:absolute;left:42px;top:172px;width:1008px;height:367px;overflow:hidden;
    background:linear-gradient(100deg,var(--hero-light),var(--hero-dark) 60%)}
  .hero-photo{position:absolute;right:0;top:0;width:480px;height:367px;
    background:linear-gradient(90deg,rgba(160,175,120,0),#c9c6bd 35%,#8e8a84 60%,#1f2430 85%,#d8d4cc)}
  .hero-title{position:absolute;left:28px;top:54px;color:#fff;font-size:50px;font-weight:400;line-height:56px;
    text-shadow:0 2px 3px rgba(0,0,0,.3)}
  .hero-lede{position:absolute;left:31px;top:200px;width:505px;color:#fff;font-size:29px;font-weight:300;line-height:35px}

  .feature{position:absolute;top:553px;width:325px;height:289px;border-radius:3px;overflow:hidden}
  .feature-photo{position:absolute;inset:0}
  .feature-tab{position:absolute;left:0;top:21px;height:38px;background:var(--tab-blue);
    color:#fff;font-size:29px;padding-left:21px;line-height:38px;white-space:nowrap}
  .feature-text{position:absolute;left:21px;top:67px;width:262px;color:#fff;font-size:19px;font-weight:500;line-height:23px}
  .feature-intro{left:42px}
  .feature-intro .feature-tab{width:222px}
  .feature-intro .feature-photo{background:linear-gradient(#f3c23c,#f6d98a 30%,#cfc9c0 55%,#6d6a6a 85%,#4a4d55)}
  .feature-gaps{left:384px}
  .feature-gaps .feature-tab{width:222px;padding-left:13px}
  .feature-gaps .feature-text{left:13px;width:270px}
  .feature-gaps .feature-photo{background:linear-gradient(#68c95c,#7fcf6c 30%,#a9b7a8 55%,#555a62 80%,#33363c)}
  .feature-plans{left:727px}
  .feature-plans .feature-tab{width:269px;padding-left:11px}
  .feature-plans .feature-text{left:11px;width:265px}
  .feature-plans .feature-photo{background:linear-gradient(#d0343a,#c8353b 30%,#7a2a35 55%,#2a2d3a 75%,#9b9aa0)}

  .service-bar{position:absolute;left:42px;top:862px;width:1010px;height:150px;border:1px solid var(--rule);
    border-radius:3px;background:linear-gradient(#fff,#ececec);display:flex}
  .service{text-align:center;border-right:1px solid var(--rule);padding-top:20px}
  .service:last-child{border-right:none}
  .service h2{font-size:36px;font-weight:400;color:var(--heading-blue);line-height:40px;margin-bottom:10px}
  .service svg{display:block;margin:0 auto}

  .site-footer{position:absolute;left:0;top:1034px;width:1092px;height:166px;background:var(--footer-bg);border-top:1px solid #d9d9d9}
  .footer-dot{position:absolute;left:57px;top:51px;width:52px;height:52px;border-radius:50%;background:var(--heading-blue)}
  .footer-nav{position:absolute;left:128px;top:32px;display:flex;list-style:none}
  .footer-nav li{font-size:17px;color:var(--footer-text);margin-right:20px}
  .footer-nav li.current{color:var(--brand-navy)}
  .footer-rights{position:absolute;left:129px;top:64px;font-size:13px;color:var(--footer-text)}
  .footer-rule{position:absolute;left:126px;top:92px;width:893px;border-top:1px solid var(--rule)}
  .footer-blurb{position:absolute;left:126px;top:103px;width:490px;font-size:11.5px;line-height:20px;color:var(--footer-text)}
  .social{position:absolute;left:852px;top:20px;display:flex;gap:7px}
  .social span{width:36px;height:36px;border-radius:5px;background:linear-gradient(#9aa9c4,#6f809e)}
  .chat{position:absolute;left:878px;top:104px;text-align:right;font-size:19px;line-height:19px}
  .chat b{display:block;font-weight:400;color:var(--chat-red)}
  .chat svg{position:absolute;left:96px;top:2px}
</style>
</head>
<body>

<nav class="main-nav">
  <ul>
    <li class="current">HOME</li><li>ABOUT</li><li>GEN 101</li><li>GEN GAPS</li><li>STRATEGIES</li>
    <li>RESOURCES</li><li>TRAINING</li><li>TOOLS</li><li>DISCUSS</li><li>CONTACT</li>
  </ul>
</nav>

<header>
  <div class="brand">
    <span class="brand-dot"></span>
    <span class="brand-name">BrightlowPath</span>
    <span class="brand-for">…for</span>
    <span class="partner-badge"></span>
  </div>
  <div class="contact">
    <div class="contact-row">
      <svg width="24" height="24" viewBox="0 0 24 24"><path d="M7 3c1 0 2 3 2 4s-2 1-2 2c0 2 4 7 6 7 1 0 1-2 2-2s4 1 4 2-2 4-4 4C9 20 4 13 4 8c0-2 2-5 3-5z" fill="none" stroke="#555" stroke-width="1.6"/></svg>
      <span class="contact-phone">888.014.2290</span>
    </div>
    <div class="contact-row">
      <svg width="24" height="16" viewBox="0 0 24 16"><rect x="1" y="1" width="22" height="14" fill="none" stroke="#555" stroke-width="1.5"/><path d="M1 1l11 8 11-8" fill="none" stroke="#555" stroke-width="1.5"/></svg>
      <span class="contact-email">info@brightlowpath.example</span>
    </div>
  </div>
</header>

<section class="hero">
  <div class="hero-photo" role="img" aria-label="Smiling businesswoman in a dark suit standing in a bright office"></div>
  <h1 class="hero-title">GENERATIONAL TOOLS &amp;<br>TRAINING FOR HR PROFESSIONALS</h1>
  <p class="hero-lede">BrightlowPath is committed to providing HR professionals with training that matters. We help you leverage the strengths of every generation.</p>
</section>

<article class="feature feature-intro">
  <div class="feature-photo" role="img" aria-label="Group of colleagues of different ages in an office"></div>
  <div class="feature-tab">Generations 101</div>
  <p class="feature-text">Learn who the generations are and why they matter.</p>
</article>
<article class="feature feature-gaps">
  <div class="feature-photo" role="img" aria-label="Coworkers gathered around a desk discussing a problem"></div>
  <div class="feature-tab">Generations Gaps</div>
  <p class="feature-text">Master the challenges created by today’s generational mix.</p>
</article>
<article class="feature feature-plans">
  <div class="feature-photo" role="img" aria-label="Hands joining puzzle pieces together"></div>
  <div class="feature-tab">Generations Strategies</div>
  <p class="feature-text">Develop successfull strategies that drive your organization.</p>
</article>

<section class="service-bar">
  <div class="service" style="width:245px">
    <h2>RESOURCES</h2>
    <svg width="64" height="56" viewBox="0 0 64 56">
      <rect x="6" y="40" width="52" height="12" rx="2" fill="#6a4aa8"/>
      <rect x="10" y="27" width="48" height="12" rx="2" fill="#d99a2b"/>
      <rect x="4" y="14" width="50" height="12" rx="2" fill="#8a3b2a"/>
      <rect x="12" y="3" width="40" height="10" rx="2" fill="#b05a2c"/>
    </svg>
  </div>
  <div class="service" style="width:263px">
    <h2>TRAINING</h2>
    <svg width="84" height="60" viewBox="0 0 84 60">
      <path d="M42 4L82 20 42 36 2 20z" fill="#2b2b2b"/>
      <path d="M20 28v14c0 6 44 6 44 0V28L42 37z" fill="#3a3a3a"/>
      <path d="M70 23v24" stroke="#f2c200" stroke-width="3"/>
      <rect x="67" y="45" width="6" height="12" fill="#f2c200"/>
    </svg>
  </div>
  <div class="service" style="width:266px">
    <h2>TOOLS</h2>
    <svg width="56" height="56" viewBox="0 0 56 56">
      <path d="M10 46L40 16" stroke="#6d7a86" stroke-width="6" stroke-linecap="round"/>
      <circle cx="42" cy="14" r="8" fill="none" stroke="#9aa6b0" stroke-width="5"/>
      <path d="M46 46L18 18" stroke="#2f6fb3" stroke-width="6" stroke-linecap="round"/>
      <rect x="8" y="8" width="16" height="10" rx="2" transform="rotate(45 16 13)" fill="#7a8691"/>
    </svg>
  </div>
  <div class="service" style="width:234px">
    <h2>DISCUSS</h2>
    <svg width="66" height="54" viewBox="0 0 66 54">
      <path d="M24 6h36a5 5 0 015 5v16a5 5 0 01-5 5H54l2 8-10-8H24a5 5 0 01-5-5V11a5 5 0 015-5z" fill="#9aa3ad"/>
      <path d="M6 18h34a5 5 0 015 5v14a5 5 0 01-5 5H18L8 50l2-8H6a5 5 0 01-5-5V23a5 5 0 015-5z" fill="#2f8fd0"/>
    </svg>
  </div>
</section>

<footer class="site-footer">
  <span class="footer-dot"></span>
  <ul class="footer-nav">
    <li class="current">Home</li><li>About</li><li>Gen 101</li><li>Gen Gaps</li><li>Strategies</li>
    <li>Resources</li><li>Training</li><li>Tools</li><li>Discuss</li><li>Contact</li>
  </ul>
  <p class="footer-rights">All Rights Reserved - 2011. www.brightlowpath.example</p>
  <div class="footer-rule"></div>
  <p class="footer-blurb">Lorem Ipsum is simply dummy text of the printing and typesetting industry. Lorem Ipsum has been the industry's standard dummy text ever since the 1500s, when an unknown printer took a galley of type and scrambled it to make a type specimen book. It has survived</p>
  <div class="social"><span></span><span></span><span></span><span></span></div>
  <div class="chat">Questions?<b>CHAT WITH US!</b>
    <svg width="46" height="36" viewBox="0 0 46 36">
      <ellipse cx="18" cy="15" rx="16" ry="12" fill="#f5c400"/>
      <ellipse cx="28" cy="20" rx="15" ry="11" fill="#f08a00"/>
      <path d="M34 28l8 6-2-9z" fill="#f08a00"/>
    </svg>
  </div>
</footer>

</body>
</html>
```